Creative Challenge - Disruptive Digital Construction Business needs an Application Design

We need an application design (4 screens).
The app will offer easy-to-use an interactive course to illustrate the latest technology to construction professionals. Kindly find the attachments.
Updates

I have just posted the contest and the deadline is tomorrow!! Please give me my original 7 days back.

Need extra days to review

Target Market(s)

Construction professionals, aged from 22 to 36, who want to learn new disruptive technologies in construction.

Colors
e667a6
b868aa
33a6d7

Requirements
Must have
• The name of the app, Velmiro, stands for “Virtual Engineering Leaders”. The user is a Velmiro, who would transform the digital construction industry. We want a design that gives that feel to the users.

```html
<!DOCTYPE html>
<html lang="en">
<head>
<meta charset="utf-8">
<title>Velmiro – Activities Listing Screen</title>
<link href="https://fonts.googleapis.com/css2?family=Quicksand:wght@400;500;600;700&display=swap" rel="stylesheet">
<style>
:root{
  --board:#5f5a61;
  --screen:#f7f7f9;
  --band:#eef0f4;
  --blue:#33a6d7;
  --navy:#2b3a67;
  --ink:#2c2f3a;
  --magenta:#a32e6e;
  --pink:#e667a6;
  --panel:#2f69a3;
  --panel-line:rgba(255,255,255,.22);
  --green:#12a14e;
  --white:#ffffff;
  --card-orange:#f8b24a;
  --card-navy:#1f2249;
  --card-red:#ee4d4a;
}
*{box-sizing:border-box;margin:0;padding:0}
html,body{width:1200px;height:1028px;overflow:hidden}
body{background:var(--board);font-family:"Quicksand",sans-serif;color:var(--white);position:relative}

.intro{position:absolute;left:400px;top:52px;width:420px}
.intro-title{font-size:13px;font-weight:700;margin-bottom:18px}
.intro-text{font-size:12.8px;font-weight:500;line-height:24px}
.intro-text b{font-weight:700}
.closing{position:absolute;left:391px;top:878px;font-size:15.5px;font-weight:500;line-height:29px}

.phone{position:absolute;top:120px;width:318px;height:695px;background:var(--screen);overflow:hidden;color:var(--ink)}
.phone-left{left:60px}
.phone-right{left:824px}

.status-bar{position:absolute;left:0;top:0;width:100%;height:19px;background:var(--white);font-size:10px;font-weight:500;display:flex;align-items:center;justify-content:space-between;padding:0 6px}
.status-bar .carrier{display:flex;align-items:center;gap:3px}
.status-bar .battery{display:flex;align-items:center;gap:5px}
.status-bar .time{position:absolute;left:50%;transform:translateX(-50%)}
.app-header{position:absolute;left:0;top:19px;width:100%;height:37px;background:var(--white);display:flex;align-items:center;padding:0 10px}
.app-header .menu-icon{margin-right:8px}
.app-header .screen-title{position:absolute;left:0;right:0;text-align:center;font-size:12px;font-weight:500;letter-spacing:.2px}
.app-header .screen-title b{font-weight:700}
.app-header .search-icon{margin-left:auto}

.subject{position:absolute;left:0;width:100%;height:24px;background:var(--band);display:flex;align-items:center;padding:0 14px 0 15px}
.subject-open{top:58px;height:28px;background:var(--screen);border-bottom:1px solid #dfe2e8}
.subject svg.icon{width:13px;height:13px;margin-right:7px;flex:none}
.subject .subject-name{font-size:10px;font-weight:600;color:var(--blue)}
.subject .chevron{margin-left:auto}

.filter-row{position:absolute;left:0;top:86px;width:100%;height:24px;display:flex;align-items:center;padding-left:16px;font-size:5.6px;font-weight:700;letter-spacing:.2px;color:var(--navy)}
.filter-row svg{margin-right:9px}
.phone-right .filter-row{color:var(--white)}

.filter-panel{position:absolute;left:0;top:86px;width:100%;height:96px;background:var(--panel);box-shadow:0 2px 3px rgba(0,0,0,.15)}
.filter-group{position:absolute;left:16px;right:23px;height:24px;border-top:1px solid var(--panel-line);font-size:5px;font-weight:500;color:var(--white)}
.filter-group span{position:absolute;top:8px;white-space:nowrap}
.filter-group .group-label{left:0;font-weight:700;font-size:5.5px}
.filter-group .active{color:var(--pink);font-weight:700}

.class-row{position:absolute;left:0;width:100%;height:23.7px;display:flex;align-items:center;padding-left:16px;font-size:7.3px;font-weight:500;color:var(--navy)}
.class-row:nth-child(odd){background:var(--band)}
.class-row b{font-weight:700;margin-right:3px}
.class-row .mark{position:absolute;right:13px;top:6px}

.sublinks{position:absolute;left:0;top:566px;width:100%;height:49px}
.sublink{position:absolute;top:0;height:49px;border-radius:3px;display:flex;align-items:center;justify-content:center;text-align:center;font-size:9px;font-weight:500;line-height:12px;color:var(--white);overflow:hidden}
.sublink-references{left:-3px;width:93px;background:linear-gradient(160deg,var(--card-orange) 55%,#3a3d6e 100%)}
.sublink-standards{left:99px;width:117px;background:linear-gradient(200deg,#f3efe9 0%,var(--card-navy) 35%,var(--card-navy) 75%,#e8574f 100%)}
.sublink-abbreviations{left:226px;width:117px;background:linear-gradient(180deg,var(--card-orange) 0%,var(--card-red) 45%,var(--card-red) 100%);justify-content:flex-start;padding-left:22px}

.annotations{position:absolute;left:0;top:0;width:1200px;height:1028px;pointer-events:none}
.note{position:absolute;font-size:10.2px;font-weight:700;line-height:18.5px;color:var(--white)}
</style>
</head>
<body>

<section class="intro">
  <h1 class="intro-title">Activities Listing Screen</h1>
  <p class="intro-text">This is the most crucial screen, so i have started to work from here. After user selects activities, page opens with the subjects regarding to it.<br>We are seeing the page which user has interacted with the <b>subject 5.1</b></p>
</section>

<!-- Left screen: collapsed filter -->
<div class="phone phone-left">
  <div class="status-bar">
    <span class="carrier">●●●○○ Velnet <svg width="9" height="7" viewBox="0 0 9 7"><path d="M.5 2.5a6 6 0 0 1 8 0M2 4a4 4 0 0 1 5 0M3.5 5.5a1.6 1.6 0 0 1 2 0" stroke="#111" fill="none" stroke-width="1"/></svg></span>
    <span class="time">9:41 AM</span>
    <span class="battery">42% <svg width="20" height="9" viewBox="0 0 20 9"><rect x=".5" y=".5" width="17" height="8" rx="1.5" fill="none" stroke="#111"/><rect x="2" y="2" width="7" height="5" fill="#111"/><rect x="18.5" y="3" width="1.2" height="3" fill="#111"/></svg></span>
  </div>
  <header class="app-header">
    <svg class="menu-icon" width="13" height="11" viewBox="0 0 13 11"><path d="M0 1h13M0 5.5h13M0 10h9" stroke="#33a6d7" stroke-width="1.4"/></svg>
    <svg width="16" height="18" viewBox="0 0 16 18"><path d="M8 1a5 5 0 0 0-5 5v5l-2 3h14l-2-3V6a5 5 0 0 0-5-5z" fill="#a32e6e"/><circle cx="8" cy="16" r="2" fill="#a32e6e"/><text x="8" y="11" font-size="8" text-anchor="middle" fill="#fff" font-family="Quicksand,sans-serif">2</text></svg>
    <div class="screen-title">ACTIVITIES <b>ISO19650</b></div>
    <svg class="search-icon" width="13" height="13" viewBox="0 0 13 13"><circle cx="5.5" cy="5.5" r="4.5" fill="none" stroke="#33a6d7" stroke-width="1.5"/><path d="M9 9l3.5 3.5" stroke="#33a6d7" stroke-width="1.6"/></svg>
  </header>

  <div class="subject subject-open">
    <svg class="icon" viewBox="0 0 14 14"><circle cx="7" cy="7" r="2.3" fill="none" stroke="#a32e6e" stroke-width="1.1"/><circle cx="7" cy="7" r="5" fill="none" stroke="#a32e6e" stroke-width="1.1" stroke-dasharray="2 1.3"/></svg>
    <span class="subject-name">5.1 Assessment &amp; Need</span>
    <svg class="chevron" width="10" height="6" viewBox="0 0 10 6"><path d="M1 1l4 4 4-4" stroke="#33a6d7" stroke-width="1.4" fill="none"/></svg>
  </div>
  <div class="filter-row"><svg width="12" height="9" viewBox="0 0 12 9"><path d="M0 1.5h12M0 4.5h12M0 7.5h12" stroke="#2b3a67" stroke-width="1"/><rect x="3" y=".3" width="2" height="2.4" fill="#2b3a67"/><rect x="7" y="3.3" width="2" height="2.4" fill="#2b3a67"/><rect x="4" y="6.3" width="2" height="2.4" fill="#2b3a67"/></svg>FILTER SUBJECTS</div>

  <div class="class-list">
    <div class="class-row" style="top:110px"><b>5.1.1</b> Appoint Individuals to undertake the information management function<svg class="mark" width="10" height="10" viewBox="0 0 10 10"><path d="M1 5.5l2.5 3L9 1" stroke="#a32e6e" stroke-width="1.4" fill="none"/></svg></div>
    <div class="class-row" style="top:133.7px"><b>5.1.2</b> Establish the project's information requirements<svg class="mark" width="9" height="9" viewBox="0 0 10 10"><path d="M5 .5l1.3 3H9.6l-2.7 2 1 3.2L5 6.8 2.1 8.7l1-3.2-2.7-2h3.3z" fill="#2f69a3"/></svg></div>
    <div class="class-row" style="top:157.4px"><b>5.1.3</b> Establish the project's information delivery milestones</div>
    <div class="class-row" style="top:181.1px"><b>5.1.4</b> Establish the project's information standards</div>
    <div class="class-row" style="top:204.8px"><b>5.1.5</b> Establish the project's information production methods and procedures</div>
    <div class="class-row" style="top:228.5px"><b>5.1.6</b> Establish the project's reference information and shared resources</div>
    <div class="class-row" style="top:252.2px"><b>5.1.7</b> Establish the project's common data environment</div>
    <div class="class-row" style="top:275.9px"><b>5.1.8</b> Establish the project's information protocol</div>
  </div>

  <div class="subject" style="top:308.6px"><svg class="icon" viewBox="0 0 14 14"><path d="M2 2.5h10M7 2.5V13M4 2.5v2M10 2.5v2" stroke="#a32e6e" stroke-width="1.1" fill="none"/></svg><span class="subject-name">5.2 Invitation to Tender</span><svg class="chevron" width="6" height="9" viewBox="0 0 6 9"><path d="M1 1l3.5 3.5L1 8" stroke="#555" stroke-width="1" fill="none"/></svg></div>
  <div class="subject" style="top:346.2px"><svg class="icon" viewBox="0 0 14 14"><path d="M6 3L1.5 7 6 11V8.5c3 0 5 .8 6.5 3-.5-3.5-2.5-6-6.5-6.5z" stroke="#a32e6e" stroke-width="1.1" fill="none"/></svg><span class="subject-name">5.3 Tender Response</span><svg class="chevron" width="6" height="9" viewBox="0 0 6 9"><path d="M1 1l3.5 3.5L1 8" stroke="#555" stroke-width="1" fill="none"/></svg></div>
  <div class="subject" style="top:383.8px"><svg class="icon" viewBox="0 0 14 14"><rect x="1.5" y="2.5" width="11" height="10" rx="1" stroke="#a32e6e" stroke-width="1.1" fill="none"/><path d="M1.5 5.5h11M4.5 1v3M9.5 1v3" stroke="#a32e6e" stroke-width="1.1"/></svg><span class="subject-name">5.4 Appointment</span><svg class="chevron" width="6" height="9" viewBox="0 0 6 9"><path d="M1 1l3.5 3.5L1 8" stroke="#555" stroke-width="1" fill="none"/></svg></div>
  <div class="subject" style="top:421.4px"><svg class="icon" viewBox="0 0 14 14"><path d="M1 1l4 4M13 1L9 5M1 13l4-4M13 13L9 9M1 1h3M1 1v3M13 1h-3M13 1v3M1 13h3M1 13v-3M13 13h-3M13 13v-3" stroke="#a32e6e" stroke-width="1.3" fill="none"/></svg><span class="subject-name">5.5 Mobilization</span><svg class="chevron" width="6" height="9" viewBox="0 0 6 9"><path d="M1 1l3.5 3.5L1 8" stroke="#555" stroke-width="1" fill="none"/></svg></div>
  <div class="subject" style="top:459px"><svg class="icon" viewBox="0 0 14 14"><path d="M7 3L2.5 11h9z" stroke="#a32e6e" stroke-width="1.1" fill="none"/><circle cx="7" cy="2.5" r="1.5" fill="#a32e6e"/><circle cx="2.5" cy="11" r="1.5" fill="#a32e6e"/><circle cx="11.5" cy="11" r="1.5" fill="#a32e6e"/></svg><span class="subject-name">5.6 Collaborative Production of Information</span><svg class="chevron" width="6" height="9" viewBox="0 0 6 9"><path d="M1 1l3.5 3.5L1 8" stroke="#555" stroke-width="1" fill="none"/></svg></div>
  <div class="subject" style="top:496.6px"><svg class="icon" viewBox="0 0 14 14"><circle cx="7" cy="6.5" r="5.5" stroke="#a32e6e" stroke-width="1.1" fill="none"/><path d="M7 3.5v4M7 9v1" stroke="#a32e6e" stroke-width="1.3"/></svg><span class="subject-name">5.7 Information Model Delivery</span><svg class="chevron" width="6" height="9" viewBox="0 0 6 9"><path d="M1 1l3.5 3.5L1 8" stroke="#555" stroke-width="1" fill="none"/></svg></div>
  <div class="subject" style="top:534.2px"><svg class="icon" viewBox="0 0 14 14"><circle cx="7" cy="7" r="5.5" stroke="#a32e6e" stroke-width="1.1" fill="none"/><path d="M4.5 7l2 2 3.5-3.5" stroke="#a32e6e" stroke-width="1.2" fill="none"/></svg><span class="subject-name">5.8 Project Close-out</span><svg class="chevron" width="6" height="9" viewBox="0 0 6 9"><path d="M1 1l3.5 3.5L1 8" stroke="#555" stroke-width="1" fill="none"/></svg></div>

  <div class="sublinks">
    <div class="sublink sublink-references" role="img" aria-label="Colourful abstract illustration for the references section">REFERENCES</div>
    <div class="sublink sublink-standards" role="img" aria-label="Colourful abstract illustration for the BIM related standards section">BIM RELATED<br>STANDARTS</div>
    <div class="sublink sublink-abbreviations" role="img" aria-label="Colourful abstract illustration for the abbreviations section">ABBREVIATIONS</div>
  </div>
</div>

<!-- Right screen: filter panel open -->
<div class="phone phone-right">
  <div class="status-bar">
    <span class="carrier">●●●○○ Velnet <svg width="9" height="7" viewBox="0 0 9 7"><path d="M.5 2.5a6 6 0 0 1 8 0M2 4a4 4 0 0 1 5 0M3.5 5.5a1.6 1.6 0 0 1 2 0" stroke="#111" fill="none" stroke-width="1"/></svg></span>
    <span class="time">9:41 AM</span>
    <span class="battery">42% <svg width="20" height="9" viewBox="0 0 20 9"><rect x=".5" y=".5" width="17" height="8" rx="1.5" fill="none" stroke="#111"/><rect x="2" y="2" width="7" height="5" fill="#111"/><rect x="18.5" y="3" width="1.2" height="3" fill="#111"/></svg></span>
  </div>
  <header class="app-header">
    <svg class="menu-icon" width="13" height="11" viewBox="0 0 13 11"><path d="M0 1h13M0 5.5h13M0 10h9" stroke="#33a6d7" stroke-width="1.4"/></svg>
    <svg width="16" height="18" viewBox="0 0 16 18"><path d="M8 1a5 5 0 0 0-5 5v5l-2 3h14l-2-3V6a5 5 0 0 0-5-5z" fill="#a32e6e"/><circle cx="8" cy="16" r="2" fill="#a32e6e"/><text x="8" y="11" font-size="8" text-anchor="middle" fill="#fff" font-family="Quicksand,sans-serif">2</text></svg>
    <div class="screen-title">ACTIVITIES <b>ISO19650</b></div>
    <svg class="search-icon" width="13" height="13" viewBox="0 0 13 13"><circle cx="5.5" cy="5.5" r="4.5" fill="none" stroke="#33a6d7" stroke-width="1.5"/><path d="M9 9l3.5 3.5" stroke="#33a6d7" stroke-width="1.6"/></svg>
  </header>

  <div class="subject subject-open">
    <svg class="icon" viewBox="0 0 14 14"><circle cx="7" cy="7" r="2.3" fill="none" stroke="#a32e6e" stroke-width="1.1"/><circle cx="7" cy="7" r="5" fill="none" stroke="#a32e6e" stroke-width="1.1" stroke-dasharray="2 1.3"/></svg>
    <span class="subject-name">5.1 Assessment &amp; Need</span>
    <svg class="chevron" width="10" height="6" viewBox="0 0 10 6"><path d="M1 1l4 4 4-4" stroke="#33a6d7" stroke-width="1.4" fill="none"/></svg>
  </div>
  <div class="filter-panel">
    <div class="filter-group" style="top:24px;border-top:0"><span class="group-label">STATUS LEVEL</span><span class="active" style="left:53px">PROJECT</span><span style="left:85px">APPOINTMENT</span></div>
    <div class="filter-group" style="top:48px"><span class="group-label">INFORMATION</span><span class="active" style="left:53px">REQUIREMENTS</span><span style="left:104px">PROCUREMENTS</span><span style="left:158px">PLANNING</span><span style="left:203px">DELIVERY</span><span style="left:248px">ARCHIVING</span></div>
    <div class="filter-group" style="top:72px"><span class="group-label">ACTOR</span><span style="left:53px">APPOINTING PARTY</span><span class="active" style="left:109px">LEAD APPOINTING PARTY</span><span style="left:181px">APPOINTED PARTY</span></div>
  </div>
  <div class="filter-row"><svg width="12" height="9" viewBox="0 0 12 9"><path d="M0 1.5h12M0 4.5h12M0 7.5h12" stroke="#fff" stroke-width="1"/><rect x="3" y=".3" width="2" height="2.4" fill="#fff"/><rect x="7" y="3.3" width="2" height="2.4" fill="#fff"/><rect x="4" y="6.3" width="2" height="2.4" fill="#fff"/></svg>FILTER SUBJECTS</div>

  <div class="class-list">
    <div class="class-row" style="top:181.1px;background:var(--screen)"><b>5.1.4</b> Establish the project's information standards</div>
    <div class="class-row" style="top:204.8px;background:var(--band)"><b>5.1.5</b> Establish the project's information production methods and procedures</div>
    <div class="class-row" style="top:228.5px;background:var(--screen)"><b>5.1.6</b> Establish the project's reference information and shared resources</div>
    <div class="class-row" style="top:252.2px;background:var(--band)"><b>5.1.7</b> Establish the project's common data environment</div>
    <div class="class-row" style="top:275.9px;background:var(--screen)"><b>5.1.8</b> Establish the project's information protocol</div>
  </div>

  <div class="subject" style="top:308.6px"><svg class="icon" viewBox="0 0 14 14"><path d="M2 2.5h10M7 2.5V13M4 2.5v2M10 2.5v2" stroke="#a32e6e" stroke-width="1.1" fill="none"/></svg><span class="subject-name">5.2 Invitation to Tender</span><svg class="chevron" width="6" height="9" viewBox="0 0 6 9"><path d="M1 1l3.5 3.5L1 8" stroke="#555" stroke-width="1" fill="none"/></svg></div>
  <div class="subject" style="top:346.2px"><svg class="icon" viewBox="0 0 14 14"><path d="M6 3L1.5 7 6 11V8.5c3 0 5 .8 6.5 3-.5-3.5-2.5-6-6.5-6.5z" stroke="#a32e6e" stroke-width="1.1" fill="none"/></svg><span class="subject-name">5.3 Tender Response</span><svg class="chevron" width="6" height="9" viewBox="0 0 6 9"><path d="M1 1l3.5 3.5L1 8" stroke="#555" stroke-width="1" fill="none"/></svg></div>
  <div class="subject" style="top:383.8px"><svg class="icon" viewBox="0 0 14 14"><rect x="1.5" y="2.5" width="11" height="10" rx="1" stroke="#a32e6e" stroke-width="1.1" fill="none"/><path d="M1.5 5.5h11M4.5 1v3M9.5 1v3" stroke="#a32e6e" stroke-width="1.1"/></svg><span class="subject-name">5.4 Appointment</span><svg class="chevron" width="6" height="9" viewBox="0 0 6 9"><path d="M1 1l3.5 3.5L1 8" stroke="#555" stroke-width="1" fill="none"/></svg></div>
  <div class="subject" style="top:421.4px"><svg class="icon" viewBox="0 0 14 14"><path d="M1 1l4 4M13 1L9 5M1 13l4-4M13 13L9 9M1 1h3M1 1v3M13 1h-3M13 1v3M1 13h3M1 13v-3M13 13h-3M13 13v-3" stroke="#a32e6e" stroke-width="1.3" fill="none"/></svg><span class="subject-name">5.5 Mobilization</span><svg class="chevron" width="6" height="9" viewBox="0 0 6 9"><path d="M1 1l3.5 3.5L1 8" stroke="#555" stroke-width="1" fill="none"/></svg></div>
  <div class="subject" style="top:459px"><svg class="icon" viewBox="0 0 14 14"><path d="M7 3L2.5 11h9z" stroke="#a32e6e" stroke-width="1.1" fill="none"/><circle cx="7" cy="2.5" r="1.5" fill="#a32e6e"/><circle cx="2.5" cy="11" r="1.5" fill="#a32e6e"/><circle cx="11.5" cy="11" r="1.5" fill="#a32e6e"/></svg><span class="subject-name">5.6 Collaborative Production of Information</span><svg class="chevron" width="6" height="9" viewBox="0 0 6 9"><path d="M1 1l3.5 3.5L1 8" stroke="#555" stroke-width="1" fill="none"/></svg></div>
  <div class="subject" style="top:496.6px"><svg class="icon" viewBox="0 0 14 14"><circle cx="7" cy="6.5" r="5.5" stroke="#a32e6e" stroke-width="1.1" fill="none"/><path d="M7 3.5v4M7 9v1" stroke="#a32e6e" stroke-width="1.3"/></svg><span class="subject-name">5.7 Information Model Delivery</span><svg class="chevron" width="6" height="9" viewBox="0 0 6 9"><path d="M1 1l3.5 3.5L1 8" stroke="#555" stroke-width="1" fill="none"/></svg></div>
  <div class="subject" style="top:534.2px"><svg class="icon" viewBox="0 0 14 14"><circle cx="7" cy="7" r="5.5" stroke="#a32e6e" stroke-width="1.1" fill="none"/><path d="M4.5 7l2 2 3.5-3.5" stroke="#a32e6e" stroke-width="1.2" fill="none"/></svg><span class="subject-name">5.8 Project Close-out</span><svg class="chevron" width="6" height="9" viewBox="0 0 6 9"><path d="M1 1l3.5 3.5L1 8" stroke="#555" stroke-width="1" fill="none"/></svg></div>

  <div class="sublinks">
    <div class="sublink sublink-references" role="img" aria-label="Colourful abstract illustration for the references section">REFERENCES</div>
    <div class="sublink sublink-standards" role="img" aria-label="Colourful abstract illustration for the BIM related standards section">BIM RELATED<br>STANDARTS</div>
    <div class="sublink sublink-abbreviations" role="img" aria-label="Colourful abstract illustration for the abbreviations section">ABBREVIATIONS</div>
  </div>
</div>

<svg class="annotations" viewBox="0 0 1200 1028" aria-hidden="true">
  <g stroke="#12a14e" stroke-width="2" fill="none">
    <path d="M311 220H423M717 220H829"/>
    <path d="M372 243H483"/>
    <path d="M372 266.5H483"/>
    <path d="M372 438V662M372 551H479"/>
    <path d="M377 720.5H479"/>
  </g>
  <g fill="#12a14e">
    <circle cx="311" cy="220" r="4"/><circle cx="423" cy="220" r="4"/><circle cx="717" cy="220" r="4"/><circle cx="829" cy="220" r="4"/>
    <circle cx="372" cy="243" r="4"/><circle cx="483" cy="243" r="4"/>
    <circle cx="372" cy="266.5" r="4"/><circle cx="483" cy="266.5" r="4"/>
    <circle cx="372" cy="438" r="4"/><circle cx="372" cy="662" r="4"/><circle cx="479" cy="551" r="4"/>
    <circle cx="479" cy="720.5" r="4"/>
  </g>
</svg>
<p class="note" style="left:441px;top:209px">Under each subject header, filter subject option appears</p>
<p class="note" style="left:493px;top:234px">User can tick the class which he/she finishes from class detail page</p>
<p class="note" style="left:493px;top:257px">User bookmarks the class from the class the detail page</p>
<p class="note" style="left:489px;top:541px">Other subjects can be opened with interaction.<br>Maintaining a closed state for the subjects gives the app<br>a much more minimal feel and easier interaction</p>
<p class="note" style="left:489px;top:711px">Sub links are compiled in a horizontal column user can slide<br>them to left / right</p>

<p class="closing">I wanted to be clear with you to continue to work on the brief.<br>Please give feedback so i can continue to build the app.</p>

</body>
</html>
```